Email Signature

We need a generic email signature designed for our buiding company called 'Birchfield Dwellings'.
We need the following included:
- Name
- Job title (Sales Consultant)
- Phone number
- Mobile number
- Email address
- Physical address
- Web addresss
Please look at the files I have uploaded as these will give you a good idea on our current branding. Our current email signature works well but just needs refreshing! I've also uploaded some images which can be used if needed.
Industry/Entity Type
It Company
Requirements
Nice to have
- If you could incorporate the colours used on the brochure example (contents list) and and arrows on the bottom of the letterhead... just a thought!

```html
<!DOCTYPE html>
<html lang="en">
<head>
<meta charset="utf-8">
<title>Birchfield Dwellings – Email Signature</title>
<link rel="stylesheet" href="https://fonts.googleapis.com/css2?family=Poppins:wght@400;600&display=swap">
<style>
  :root {
    --brand-red: #9b1200;
    --stone: #5e504a;
    --plum: #5a1c44;
    --navy: #2b2a55;
    --ink: #1a1a1a;
    --paper: #ffffff;
  }
  * { margin: 0; padding: 0; box-sizing: border-box; }
  html, body {
    width: 1200px;
    height: 800px;
    overflow: hidden;
    background: var(--paper);
  }
  .signature {
    position: relative;
    width: 1200px;
    height: 800px;
    background: var(--paper);
    font-family: "Poppins", "Century Gothic", sans-serif;
    color: var(--ink);
  }
  .brand {
    position: absolute;
    left: 360px;
    top: 76px;
    height: 85px;
    display: flex;
    align-items: center;
    gap: 22px;
  }
  .brand-square {
    width: 80px;
    height: 80px;
    background: var(--brand-red);
  }
  .brand-name {
    font-size: 54px;
    font-weight: 400;
    line-height: 85px;
    color: var(--brand-red);
    white-space: nowrap;
  }
  .person {
    position: absolute;
    left: 68px;
    top: 252px;
  }
  .person-name {
    font-size: 36px;
    font-weight: 600;
    color: var(--brand-red);
    line-height: 48px;
    white-space: nowrap;
  }
  .person-role {
    font-size: 34px;
    font-weight: 400;
    line-height: 48px;
    white-space: nowrap;
  }
  .contact {
    position: absolute;
    left: 68px;
    top: 392px;
    list-style: none;
    font-size: 32px;
    line-height: 40.6px;
    letter-spacing: 0.3px;
    white-space: nowrap;
  }
  .contact-label { color: var(--brand-red); }
  .contact-value { color: var(--ink); }
  .colour-band {
    position: absolute;
    left: 0;
    top: 627px;
    width: 1200px;
    height: 173px;
    background: linear-gradient(180deg,
      var(--brand-red) 0%,
      var(--stone) 35%,
      var(--plum) 60%,
      var(--navy) 80%,
      var(--brand-red) 100%);
  }
</style>
</head>
<body>
  <main class="signature">
    <header class="brand">
      <span class="brand-square"></span>
      <span class="brand-name">Birchfield Dwellings</span>
    </header>

    <section class="person">
      <p class="person-name">Name and Lastname</p>
      <p class="person-role">Sales Consultant</p>
    </section>

    <ul class="contact">
      <li><span class="contact-label">Phone</span> <span class="contact-value">03 5550 1824</span></li>
      <li><span class="contact-label">Mobile</span> <span class="contact-value">0400 218 637</span></li>
      <li><span class="contact-label">Email</span> <span class="contact-value">yourname@birchfielddwellings.com</span></li>
      <li><span class="contact-label">Adress</span> <span class="contact-value">18 Foundry Lane, Ashdale Victoria 3990</span></li>
      <li><span class="contact-label">Web</span> <span class="contact-value">www.birchfielddwellings.com</span></li>
    </ul>

    <div class="colour-band" role="img" aria-label="Decorative band of brand colours: red, stone, plum and navy"></div>
  </main>
</body>
</html>
```